Rural photograpy business card design

I need a business card for my photography business, marisol dovey photography. I would like my logo and pre designed font used on the card. Also my business specialises in photographing rural australia (e.g. shearing sheds, livestock, landscapes, farms), so a rural or country feel to the card would be great. I would like to keep the colours fresh but not too overpowering or juvenile.

Hi,

Could you please add my facebook page to the card - www.snapfolk.net/Marisol/Dovey/Photography.
Thanks,
Marisol.

Reason: I have uploaded two photos I would like either one used on the card.

Target Market(s)

Farmers, country people from their mid twenties onwards

Industry/Entity Type

Business

Contact Information for Business Card

Marisol Dovey Photography. Marisol Pendergast. 1295 Wirrabilla-Kontee Road, Kontee Qld 4871. 0471620394.

Requirements
Must have
• My pre-designed logo and font. Also please add my facebook address - www.snapfolk.net/MarisolDovey/Photography.
Please use one of the photos I have provided.
Should not have
• Peoples faces on the card.

```html
<!DOCTYPE html>
<html lang="en">
<head>
<meta charset="utf-8">
<title>Marisol Dovey Photography – Business Card</title>
<link href="https://fonts.googleapis.com/css2?family=Questrial&display=swap" rel="stylesheet">
<style>
  :root {
    --backdrop: #2a2a2a;
    --red: #cc3520;
    --red-deep: #a9241a;
    --red-shadow: #8f1c14;
    --grass: #7a1710;
    --cream: #f4dfa6;
    --paper: #ffffff;
    --paper-shade: #e4e4e4;
    --ink: #5b4a42;
    --band-text: #f6d2bd;
  }
  * { margin: 0; padding: 0; box-sizing: border-box; }
  html, body {
    width: 1200px; height: 900px; overflow: hidden;
    background: var(--backdrop);
    font-family: "Questrial", "Century Gothic", sans-serif;
  }
  .canvas {
    position: relative; width: 1200px; height: 900px;
    display: flex; flex-direction: column; align-items: center; justify-content: center; gap: 48px;
  }
  .card {
    position: relative; width: 640px; height: 366px; overflow: hidden;
    box-shadow: 0 10px 30px rgba(0,0,0,.55);
  }

  /* Front */
  .card--front {
    background: linear-gradient(160deg, var(--red) 0%, #c22e1d 55%, var(--red-deep) 100%);
  }
  .front__photo {
    position: absolute; left: 0; right: 0; bottom: 0; height: 58%;
    background:
      linear-gradient(180deg, rgba(122,23,16,0) 0%, rgba(122,23,16,.35) 30%, rgba(122,23,16,.7) 70%, var(--grass) 100%);
  }
  .front__mark {
    position: absolute; left: 0; right: 0; top: 70px; z-index: 1;
    display: flex; flex-direction: column; align-items: center; gap: 18px;
  }
  .brand-dot { width: 64px; height: 64px; border-radius: 50%; border: 6px solid var(--cream); }
  .brand-name {
    color: var(--cream); text-align: center; font-size: 34px; letter-spacing: 3px; line-height: 1.2;
    text-transform: uppercase;
  }

  /* Back */
  .card--back {
    background: linear-gradient(160deg, var(--paper) 0%, #f4f4f4 55%, var(--paper-shade) 100%);
  }
  .back__mark {
    position: absolute; left: 0; right: 0; top: 28px;
    display: flex; flex-direction: column; align-items: center; gap: 10px;
  }
  .back__mark .brand-dot { width: 46px; height: 46px; border-width: 5px; border-color: var(--red); }
  .back__mark .brand-name { color: var(--red); font-size: 27px; letter-spacing: 2px; }
  .contact {
    position: absolute; left: 0; right: 0; top: 180px; text-align: center; color: var(--ink);
  }
  .contact__name { font-size: 27px; letter-spacing: .5px; }
  .contact__phone { font-size: 18px; letter-spacing: 1px; margin-top: 4px; }
  .contact__web { font-size: 15px; letter-spacing: .5px; margin-top: 8px; color: var(--red-deep); }
  .address-band {
    position: absolute; left: 0; right: 0; bottom: 0; height: 52px;
    background: linear-gradient(90deg, var(--red-deep), var(--red));
    display: flex; align-items: center; justify-content: center;
    color: var(--band-text); font-size: 16px; letter-spacing: .5px;
  }
</style>
</head>
<body>
<main class="canvas">
  <section class="card card--front" aria-label="Business card front">
    <div class="front__photo" role="img" aria-label="Rural photograph of silhouetted paddock grasses and reeds in deep red tones"></div>
    <div class="front__mark">
      <span class="brand-dot" aria-hidden="true"></span>
      <p class="brand-name">Marisol Dovey<br>Photography</p>
    </div>
  </section>

  <section class="card card--back" aria-label="Business card back">
    <div class="back__mark">
      <span class="brand-dot" aria-hidden="true"></span>
      <p class="brand-name">Marisol Dovey<br>Photography</p>
    </div>
    <div class="contact">
      <p class="contact__name">Marisol Pendergast</p>
      <p class="contact__phone">0471 620 394</p>
      <p class="contact__web">www.snapfolk.net/MarisolDovey/Photography</p>
    </div>
    <footer class="address-band">1295 Wirrabilla-Kontee Road, Kontee Qld 4871</footer>
  </section>
</main>
</body>
</html>
```